Faith Based Film Production Ecommerce Site Needed

We are a faith based film production company that offers coaching services as well as physical and digital products.

We have a Wordpress site on Hostwick. It currently, features a landing page (https://plumfernstudio.com/), however we now need a fully fleshed out interactive website that will feature short videos/trailers as well the ability for customers to make online purchases.

The updated site will feature 5 tabs - Take 1, Take 2, Take 3, BTS and Contact. This toolbar/menu should remain fixed/stable while visitors navigate the different tabs/pages, as shown here - https://dowgenbarsk.com/ (note this site is JUST a reference for its unmoving menu/toolbar in the top right corner of the page).

The text for each tab and actual video content will be provided for potential candidates. Until then, please improvise.

There will be 5 short trailers/reels featured under the "Take 2" tab, that will be shown as thumbnails the same size found here - https://dowgenbarsk.com/see-dowgen-at-work/ (reference for thumbnail size only). The names of these trailers will be called, Lantern Quest, Lantern Blooming, Lantern Dawn, Lantern Hearth, and Lantern Courtship.

Lastly, when arriving onto the page, visitors will be greeted with a inaudible video loop, similar to the one found here - https://www.tq-moviecraft.com/ (Note - this is a reference simply to show inaudible video looping). The ACTUAL video to be used however can be found here - https://clipvault.example/manage/videos/493817265, beginning at the 15 second mark when the 3 people are entering the cinema and ending at the 28 second mark where the screen gradually fades to black. The video will then consistently re-loop.

Once again, more detail will be provided for the most interesting submissions and of course, official winner.

Should you have any questions until then, please do not hesitate to reach out.

```html
<!DOCTYPE html>
<html lang="en">
<head>
<meta charset="utf-8">
<title>Plum Fern Studio — Faith Based Film Production</title>
<link href="https://fonts.googleapis.com/css2?family=Poppins:wght@400;500;600;700;800;900&display=swap" rel="stylesheet">
<style>
:root{
  --red:#e5101d;
  --ink:#111111;
  --paper:#efefef;
  --white:#ffffff;
  --muted:#bdbdbd;
  --night:#0b1433;
  --deep:#16070a;
}
*{box-sizing:border-box;margin:0;padding:0}
html,body{width:1200px;height:3772px;overflow:hidden}
body{position:relative;font-family:"Poppins",sans-serif;background:var(--paper);color:var(--ink)}
.abs{position:absolute}

/* header */
.site-header{position:absolute;left:0;top:0;width:1200px;height:40px;z-index:5;display:flex;align-items:center;justify-content:space-between;padding:0 60px;background:rgba(5,8,20,.55)}
.brand{display:flex;align-items:center;gap:8px;color:var(--white);font-weight:700;font-size:13px;letter-spacing:1px;text-transform:uppercase}
.brand-dot{width:14px;height:14px;background:var(--white)}
.main-nav{display:flex;align-items:center;gap:18px;font-size:12px;color:var(--white);font-weight:500}
.nav-icons{display:flex;gap:12px;margin-left:14px}

/* hero */
.hero{position:absolute;left:0;top:0;width:1200px;height:600px;background:linear-gradient(120deg,#0d1a4a 0%,#1b2f7a 35%,#0a1030 70%,#050814 100%)}
.hero-title{position:absolute;left:120px;top:150px;font-size:78px;font-weight:900;letter-spacing:6px;color:var(--white);text-transform:uppercase;line-height:1}
.hero-text{position:absolute;left:122px;top:246px;width:420px;font-size:15px;line-height:1.55;color:#e4e7f2}
.btn{position:absolute;display:flex;align-items:center;justify-content:center;font-size:15px;font-weight:600;border-radius:4px}
.btn-red{background:var(--red);color:var(--white)}
.btn-white{background:var(--white);color:var(--ink)}
.watch-trailer{position:absolute;left:822px;top:270px;display:flex;align-items:center;gap:12px;color:var(--white);font-size:14px;letter-spacing:2px;text-transform:uppercase}
.dots{position:absolute;top:548px;left:488px;display:flex;gap:16px}
.dots span{width:56px;height:4px;background:rgba(255,255,255,.4)}
.dots span.on{background:var(--white)}

/* rows */
.row-title{position:absolute;left:120px;font-size:34px;font-weight:700}
.view-all{position:absolute;right:120px;font-size:16px;color:var(--red);font-weight:600}
.card{position:absolute;width:224px;height:144px;border-radius:4px;overflow:hidden}
.card-label{position:absolute;left:16px;bottom:22px;color:var(--white);font-size:13px;font-weight:600;line-height:1.2}
.card-label small{display:block;font-size:10px;font-weight:400;color:#ddd}

/* bts */
.bts{position:absolute;left:120px;top:1192px;width:960px;height:648px;border-radius:8px;background:linear-gradient(110deg,#1a0508 0%,#4a0a14 40%,#8a1024 60%,#200608 100%);overflow:hidden}
.bts-heading{position:absolute;left:40px;top:30px;color:var(--white);font-size:22px;font-weight:500}
.bts-item{position:absolute;left:0;width:392px;height:168px;background:rgba(0,0,0,.55)}
.bts-item h3{position:absolute;left:40px;top:38px;color:var(--white);font-size:24px;font-weight:700}
.bts-item p{position:absolute;left:40px;top:74px;color:var(--white);font-size:13px}
.bts-item .play{position:absolute;left:40px;top:104px;width:96px;height:28px;font-size:11px;background:var(--red);color:var(--white);border-radius:3px;display:flex;align-items:center;justify-content:center;gap:5px;font-weight:600}

/* testimonial */
.testimonial{position:absolute;left:0;top:2172px;width:1200px;height:628px;background:linear-gradient(100deg,#2a0408 0%,#140204 45%,#3a060c 100%)}
.testimonial h2{position:absolute;left:120px;top:140px;color:var(--white);font-size:34px;font-weight:700}
.stars{position:absolute;left:120px;top:196px;display:flex;gap:4px;align-items:center;color:var(--white);font-size:11px}
.person{position:absolute;left:120px;top:226px;color:var(--white);font-size:20px;font-weight:700}
.role{position:absolute;left:120px;top:256px;color:#ddd;font-size:13px}
.quote{position:absolute;left:120px;top:282px;width:470px;color:#eee;font-size:14px;line-height:1.55;font-style:italic}
.testi-photo{position:absolute;left:612px;top:136px;width:468px;height:352px;border-radius:8px;background:linear-gradient(135deg,#f7c7d2,#f2a6b8 60%,#e98aa2)}

/* contact */
.contact{position:absolute;left:0;top:2800px;width:1200px;height:720px;background:var(--white)}
.contact-frame{position:absolute;left:200px;top:100px;width:440px;height:536px;border:2px dashed #333;border-radius:4px}
.contact-red{position:absolute;left:160px;top:88px;width:460px;height:520px;background:var(--red)}
.contact-photo{position:absolute;left:120px;top:68px;width:480px;height:500px;background:linear-gradient(160deg,#5a5a5a,#2e2e2e 70%,#222)}
.contact h2{position:absolute;left:692px;top:80px;font-size:34px;font-weight:700}
.field{position:absolute;left:688px;width:384px;background:#e9e9e9;font-size:16px;color:#333;padding:0 26px;display:flex;align-items:center}
.field.tall{align-items:flex-start;padding-top:20px}

/* footer */
.site-footer{position:absolute;left:0;top:3520px;width:1200px;height:252px;background:#050505;color:var(--white)}
.foot-brand{position:absolute;left:120px;top:28px;display:flex;align-items:center;gap:8px;font-size:14px;font-weight:700;letter-spacing:1px;text-transform:uppercase}
.foot-copy{position:absolute;left:120px;top:70px;width:400px;font-size:11px;line-height:1.7;color:var(--muted)}
.foot-links{position:absolute;left:560px;top:38px;list-style:none;font-size:13px;line-height:1.72}
.follow{position:absolute;left:752px;top:38px;font-size:13px}
.socials{position:absolute;left:752px;top:66px;display:flex;gap:10px}
.socials span{width:30px;height:30px;border-radius:50%;background:var(--white)}
.app-title{position:absolute;left:752px;top:110px;font-size:13px}
.badge{position:absolute;top:140px;width:112px;height:34px;border:1px solid #777;border-radius:6px;background:#111}
</style>
</head>
<body>

<section class="hero" role="img" aria-label="Video still: three people walking into a dim blue-lit cinema"></section>
<header class="site-header">
  <div class="brand"><span class="brand-dot"></span>Plum Fern Studio</div>
  <nav class="main-nav">
    <span>Home</span><span>Take 1</span><span>Take 2</span><span>Take 3</span><span>BTS</span><span>Contact</span>
    <span class="nav-icons">
      <svg width="14" height="14" viewBox="0 0 14 14"><circle cx="7" cy="7" r="7" fill="#fff"/></svg>
      <svg width="14" height="14" viewBox="0 0 14 14" fill="none" stroke="#fff" stroke-width="1.8"><circle cx="6" cy="6" r="4.5"/><path d="M9.5 9.5 13 13"/></svg>
      <svg width="15" height="14" viewBox="0 0 15 14" fill="#fff"><path d="M0 1h3l2 8h8l2-6H4.5"/><circle cx="6" cy="12" r="1.4"/><circle cx="12" cy="12" r="1.4"/></svg>
    </span>
  </nav>
</header>
<h1 class="hero-title">Plum Fern</h1>
<p class="hero-text">Lorem ipsum dolor sit amet, consectetur adipiscing elit, sed do eiusmod tempor incididunt ut labore et dolore magna aliqua. Quis ipsum suspendisse ultrices gravida. Risus commodo viverra maecenas accumsan lacus.</p>
<a class="btn btn-red" style="left:120px;top:374px;width:130px;height:44px">Watch Now</a>
<a class="btn btn-white" style="left:268px;top:374px;width:150px;height:44px">Discover More</a>
<div class="watch-trailer">
  <svg width="48" height="48" viewBox="0 0 48 48" fill="none" stroke="#fff" stroke-width="2"><circle cx="24" cy="24" r="22"/><path d="M19 15 33 24 19 33Z" fill="#fff"/></svg>
  Watch Trailer
</div>
<div class="dots"><span></span><span class="on"></span><span></span></div>

<!-- Take 1 -->
<h2 class="row-title" style="top:656px">Take 1</h2>
<a class="view-all" style="top:668px">View All</a>
<div class="card" style="left:120px;top:728px;background:linear-gradient(135deg,#2a2a2a,#5c4a3a)" role="img" aria-label="Thumbnail: presenter filming a set video"><div class="card-label">Set Video<small>30mins</small></div></div>
<div class="card" style="left:360px;top:728px;background:linear-gradient(135deg,#3b2a2a,#7a5a50)" role="img" aria-label="Thumbnail: makeup session"><div class="card-label">Makeup Session<small>30mins</small></div></div>
<div class="card" style="left:600px;top:728px;background:linear-gradient(135deg,#1f2a36,#4a5a66)" role="img" aria-label="Thumbnail: gym shoot"><div class="card-label">Gym Shoot Video<small>30mins</small></div></div>
<div class="card" style="left:840px;top:728px;background:linear-gradient(135deg,#3a3020,#8a6a3a)" role="img" aria-label="Thumbnail: painting lesson"><div class="card-label">Learn Painting<small>30mins</small></div></div>

<!-- Take 2 -->
<h2 class="row-title" style="top:920px">Take 2</h2>
<a class="view-all" style="top:932px">View All</a>
<div class="card" style="left:120px;top:988px;background:linear-gradient(135deg,#3a1a5a,#b04a9a)" role="img" aria-label="Trailer thumbnail in purple light"><div class="card-label">Lantern Quest<small>30mins</small></div></div>
<div class="card" style="left:360px;top:988px;background:linear-gradient(135deg,#2a1a1a,#6a4030)" role="img" aria-label="Trailer thumbnail with camera operator"><div class="card-label">Lantern Blooming<small>30mins</small></div></div>
<div class="card" style="left:600px;top:988px;background:linear-gradient(135deg,#4a2a2a,#a06a5a)" role="img" aria-label="Trailer thumbnail, warm portrait"><div class="card-label">Lantern Dawn<small>30mins</small></div></div>
<div class="card" style="left:840px;top:988px;background:linear-gradient(135deg,#2a2a2a,#6a5a50)" role="img" aria-label="Trailer thumbnail, filming indoors"><div class="card-label">Lantern Hearth<small>30mins</small></div></div>

<!-- Behind the scenes -->
<section class="bts" role="img" aria-label="Camera operator in a cap filming under red light">
  <h2 class="bts-heading">Behind The Scenes</h2>
  <div class="bts-item" style="top:80px"><h3>Camera Setup</h3><p>45 mins</p><span class="play"><svg width="8" height="8" viewBox="0 0 8 8"><path d="M1 0 8 4 1 8Z" fill="#fff"/></svg>Play Now</span></div>
  <div class="bts-item" style="top:260px"><h3>Touch-Up Session</h3><p>55 mins</p><span class="play"><svg width="8" height="8" viewBox="0 0 8 8"><path d="M1 0 8 4 1 8Z" fill="#fff"/></svg>Play Now</span></div>
  <div class="bts-item" style="top:448px;background:linear-gradient(90deg,rgba(0,0,0,.6),rgba(20,90,40,.6))"><h3>Green Screen</h3><p>45 mins</p><span class="play"><svg width="8" height="8" viewBox="0 0 8 8"><path d="M1 0 8 4 1 8Z" fill="#fff"/></svg>Play Now</span></div>
</section>

<!-- Take 3 -->
<h2 class="row-title" style="top:1900px">Take 3</h2>
<a class="view-all" style="top:1912px">View All</a>
<div class="card" style="left:120px;top:1964px;background:linear-gradient(135deg,#c98a2a,#e8c070)" role="img" aria-label="Product video thumbnail"><div class="card-label">Product Video<small>30mins</small></div></div>
<div class="card" style="left:360px;top:1964px;background:linear-gradient(135deg,#8a8a8a,#d0d0d0)" role="img" aria-label="Yoga video thumbnail"><div class="card-label">Yoga Video<small>30mins</small></div></div>
<div class="card" style="left:600px;top:1964px;background:linear-gradient(135deg,#3a3a3a,#8a8a8a)" role="img" aria-label="Short movie clapperboard thumbnail"><div class="card-label">Short Movie<small>30mins</small></div></div>
<div class="card" style="left:840px;top:1964px;background:linear-gradient(135deg,#5a2a3a,#c07a8a)" role="img" aria-label="Fashion show thumbnail"><div class="card-label">Fashion Show<small>30mins</small></div></div>

<!-- Testimonial -->
<section class="testimonial">
  <h2>Testimonial</h2>
  <div class="stars">
    <svg width="90" height="16" viewBox="0 0 90 16" fill="#e5101d"><path id="s" d="M8 0 10 5.5 16 6 11.3 9.8 13 16 8 12.5 3 16 4.7 9.8 0 6 6 5.5Z"/><use href="#s" x="18"/><use href="#s" x="36"/><use href="#s" x="54"/><use href="#s" x="72"/></svg>
    <span>4.5/5 Based on 1k ratings</span>
  </div>
  <p class="person">Mirela Castaño</p>
  <p class="role">Model and Actress</p>
  <p class="quote">"Lorem ipsum dolor sit amet, consectetur adipiscing elit, sed do eiusmod tempor incididunt ut labore et dolore magna aliqua. Quis ipsum suspendisse ultrices gravida. Risus commodo viverra maecenas accumsan lacus vel facilisis."</p>
  <a class="btn btn-red" style="left:120px;top:446px;width:120px;height:40px">View All</a>
  <div class="testi-photo" role="img" aria-label="Two friends smiling over a tablet on a pink backdrop"></div>
</section>

<!-- Contact -->
<section class="contact">
  <div class="contact-frame"></div>
  <div class="contact-red"></div>
  <div class="contact-photo" role="img" aria-label="Woman posing in front of a phone on a tripod"></div>
  <h2>Get in touch!</h2>
  <div class="field" style="top:140px;height:60px">Name</div>
  <div class="field" style="top:240px;height:60px">Email Address</div>
  <div class="field tall" style="top:312px;height:96px">Event Details</div>
  <div class="field tall" style="top:432px;height:148px">Your Message</div>
  <a class="btn btn-red" style="left:688px;top:604px;width:110px;height:46px">Submit</a>
</section>

<!-- Footer -->
<footer class="site-footer">
  <div class="foot-brand"><span class="brand-dot"></span>Plum Fern Studio</div>
  <p class="foot-copy">© 2023 Company Name. All Rights Reserved. All videos and shows on this platform are trademarks of, and all related images and content are the property of, Plum Fern Studio. Duplication and copy of this is strictly prohibited. All rights reserved.</p>
  <ul class="foot-links"><li>Contact Us</li><li>Terms Of Use</li><li>Privacy Policy</li><li>Blog</li><li>FAQ</li><li>Watch List</li></ul>
  <p class="follow">Follow Us</p>
  <div class="socials"><span></span><span></span><span></span><span></span></div>
  <p class="app-title">Plum Fern Studio App</p>
  <div class="badge" style="left:752px"></div>
  <div class="badge" style="left:878px"></div>
</footer>

</body>
</html>
```